Label Design for RTD Cocktail Line Tolvanu Cellars

Tolvanu Cellars is a line of Indian-inspired artisan cocktails that "brings the bartender home" for professional men and women who like the finer things in life but don’t always have the time to treat themselves. No need for a multitude of expensive and hard-to-find ingredients, time consuming recipes, or a mixologist.

Our line of 3 open and serve cocktails blends a range of premium spirits with exotic ingredients so you can conveniently raise a glass for any of life’s celebrations.

Our bottle is the 750ml Claret bottle with Quorlex (screw cap) closure and will be covered entirely in a shrink sleeve (so potentially anything can be designed for any part of the bottle). We want the bottle to pop on the shelf so it should look different than what’s already out there (Velvet Fawn, Korvadel, Mirelda ready to drink cocktails). We are looking for a sexy design that's polished/sleek.
Updates

Reason: Hello designers! Tolvanu Cellars is so impressed with what we have received thus far and we would like to give some of the designers a few extra days to make the edits we requested. It's never too late to submit! Thank you all!

Requirements
Must have
• Front of bottle
* “Tolvanu Cellars” name and Peacock Logo- but feel free to pull the elements apart and use them on the bottle in different ways
* Open & Serve
* 12% ALC/VOL
* 750 ml
* 3 different labels in a theme for
-Brovanza
-Zestrovino
-Florquena

Brovanza Ideas- soft brown palate, the ingredients in chai spice (cloves, cardamom pods, nutmeg, black peppercorns, star anise, and cinnamon stick)

Zestrovino Ideas -cool and refreshing, pale green shade (not clashing with logo), graphics of fresh mint leaves, green chili, lime, cucumber

Florquena Ideas- soft/pale pink shades, graphics of lychi fruit (outer red shell and inner pink flesh), ginger

Back of bottle
* explanation of the 3 cocktails
Brovanza: Forget what you think you know about chai, this is not the Queen’s tea-time drink! Brovanza is a smooth, sweetly -spiced cocktail made with vodka, black tea, and a combination of aromatic spices. This velvety cocktail is rich without being heavy. Enjoy chilled or over ice anytime.

Zestrovino: Zestrovino can’t make up its mind! This fusion of zesty lime, sweet mint, earthy cucumber and spicy chilies is so refreshing you’ll crave it on a hot summer day or a cool winter’s night. The exotic botanicals in gin add a complexity to the cocktail making this a refreshing but potent drink! Enjoy chilled or over ice anytime.

Florquena: East meet West. Delicate lychi meet hard-hitting whiskey. Florquena will tempt you senses with flavor, fragrance and beauty. The peppery kick of ginger and the intensity of the un-aged whiskey are softened by lychi’s intoxicating scent and subtle, sweet finish.

Please include
1. Bottled By PQR Spirits Company
2. Sample barcode (where you would place it in your design)
3. www.TolvanuCellars.example
4. GOVERNMENT WARNING: (1) According to the Surgeon General, women should not drink alcoholic beverages during pregnancy because of the risk of birth defects. (2) Consumption of alcoholic beverages impairs your ability to drive a car or operate machinery, and may cause health problems.

Optional to include
*"Bring the Bartender Home"
*"Tolvanu Cellars” name and Peacock Logo on the back
*Entirely black sleeve with contrasting design

FYI the Fonts used in our logo are Geosans Light and Prakrta, but feel free to use other complimentary fonts on the other aspects.
Nice to have
• Optional to include

```html
<!DOCTYPE html>
<html lang="en">
<head>
<meta charset="utf-8">
<title>Tolvanu Cellars – Open &amp; Serve Cocktail Labels</title>
<link rel="stylesheet" href="https://fonts.googleapis.com/css2?family=Cormorant+Garamond:wght@500;600&family=Parisienne&family=Oswald:wght@500&display=swap">
<style>
  :root {
    --canvas: #ffffff;
    --sleeve-edge: #cfd1d4;
    --sleeve-mid: #eff0f1;
    --cap: #111111;
    --band-gold: #9a9048;
    --brand-teal: #2b8fb3;
    --ink-body: #3a3a3a;
    --zest: #3d8a4c;
    --zest-art: #4fae4a;
    --brov: #8e3b36;
    --brov-art: #8a6a4a;
    --flor: #c94459;
    --flor-art: #ec9aa3;
  }
  * { margin: 0; padding: 0; box-sizing: border-box; }
  html, body { width: 1200px; height: 860px; overflow: hidden; background: var(--canvas); }
  .canvas { position: relative; width: 1200px; height: 860px; }

  .bottle { position: absolute; top: 44px; width: 200px; height: 740px; }
  .bottle--zest { left: 96px; }
  .bottle--brov { left: 498px; }
  .bottle--flor { left: 896px; }
  .bottle-shape { position: absolute; inset: 0; width: 200px; height: 740px; }

  .neck-band {
    position: absolute; left: 70px; top: 82px; width: 60px; height: 44px;
    overflow: hidden; display: flex; align-items: center; justify-content: center;
    border-top: 2px solid var(--band-gold); border-bottom: 2px solid var(--band-gold);
  }
  .neck-band span {
    font-family: "Oswald", sans-serif; font-weight: 500; font-size: 20px;
    color: var(--band-gold); white-space: nowrap; letter-spacing: -0.5px;
  }

  .brand {
    position: absolute; left: 0; width: 200px; top: 318px; text-align: center;
    font-family: "Cormorant Garamond", serif; font-weight: 600; color: var(--brand-teal);
  }
  .brand-name { display: block; font-size: 30px; line-height: 1; }
  .brand-sub { display: block; font-size: 11px; letter-spacing: 4px; margin-top: 2px; }

  .flavour {
    position: absolute; left: 0; width: 200px; top: 412px; text-align: center;
    font-family: "Parisienne", cursive; font-size: 32px; line-height: 1;
  }
  .notes {
    position: absolute; left: 12px; width: 176px; top: 468px; text-align: center;
    font-family: "Parisienne", cursive; font-size: 13px; line-height: 1.35;
  }
  .bottle--zest .flavour, .bottle--zest .notes { color: var(--zest); }
  .bottle--brov .flavour, .bottle--brov .notes { color: var(--brov); }
  .bottle--flor .flavour, .bottle--flor .notes { color: var(--flor); }

  .medallion {
    position: absolute; left: 44px; top: 544px; width: 112px; height: 112px; border-radius: 50%;
  }
  .bottle--zest .medallion { background: radial-gradient(circle, var(--zest-art) 0%, #7cc66e 55%, rgba(124,198,110,0) 72%); }
  .bottle--brov .medallion { background: radial-gradient(circle, var(--brov-art) 0%, #b59a78 50%, rgba(181,154,120,0) 72%); }
  .bottle--flor .medallion { background: radial-gradient(circle, var(--flor-art) 0%, #f2b5bb 52%, rgba(242,181,187,0) 72%); }

  .specs {
    position: absolute; left: 20px; right: 20px; top: 694px;
    display: flex; justify-content: space-between;
    font-family: "Cormorant Garamond", serif; font-weight: 500; font-size: 12px; color: var(--ink-body);
  }
</style>
</head>
<body>
<main class="canvas">

  <section class="bottle bottle--zest">
    <svg class="bottle-shape" viewBox="0 0 200 740" aria-hidden="true">
      <defs>
        <linearGradient id="sleeve" x1="0" x2="1" y1="0" y2="0">
          <stop offset="0" stop-color="var(--sleeve-edge)"/>
          <stop offset="0.45" stop-color="var(--sleeve-mid)"/>
          <stop offset="1" stop-color="var(--sleeve-edge)"/>
        </linearGradient>
      </defs>
      <path d="M70 60 L130 60 L130 190 C130 230 200 240 200 300 L200 712 Q200 728 184 728 L16 728 Q0 728 0 712 L0 300 C0 240 70 230 70 190 Z" fill="url(#sleeve)"/>
      <rect x="66" y="0" width="68" height="64" rx="6" fill="var(--cap)"/>
    </svg>
    <div class="neck-band"><span>OPEN&amp;SERVE</span></div>
    <p class="brand"><span class="brand-name">Tolvanu</span><span class="brand-sub">CELLARS</span></p>
    <h2 class="flavour">zestrovino</h2>
    <p class="notes">Brovanza Visuales: paladar blando marrón, gráficos de clavo de olor, canela, anís estrellado, otras especias chai</p>
    <div class="medallion" role="img" aria-label="Green mint leaf and lime burst illustration"></div>
    <p class="specs"><span>12% alc/vol</span><span>750 ml</span></p>
  </section>

  <section class="bottle bottle--brov">
    <svg class="bottle-shape" viewBox="0 0 200 740" aria-hidden="true">
      <path d="M70 60 L130 60 L130 190 C130 230 200 240 200 300 L200 712 Q200 728 184 728 L16 728 Q0 728 0 712 L0 300 C0 240 70 230 70 190 Z" fill="url(#sleeve)"/>
      <rect x="66" y="0" width="68" height="64" rx="6" fill="var(--cap)"/>
    </svg>
    <div class="neck-band"><span>OPEN&amp;SERVE</span></div>
    <p class="brand"><span class="brand-name">Tolvanu</span><span class="brand-sub">CELLARS</span></p>
    <h2 class="flavour">brovanza</h2>
    <p class="notes">Brovanza Visuales: paladar blando marrón, gráficos de clavo de olor, canela, anís estrellado, otras especias chai</p>
    <div class="medallion" role="img" aria-label="Brown chai spice swirl illustration"></div>
    <p class="specs"><span>12% alc/vol</span><span>750 ml</span></p>
  </section>

  <section class="bottle bottle--flor">
    <svg class="bottle-shape" viewBox="0 0 200 740" aria-hidden="true">
      <path d="M70 60 L130 60 L130 190 C130 230 200 240 200 300 L200 712 Q200 728 184 728 L16 728 Q0 728 0 712 L0 300 C0 240 70 230 70 190 Z" fill="url(#sleeve)"/>
      <rect x="66" y="0" width="68" height="64" rx="6" fill="var(--cap)"/>
    </svg>
    <div class="neck-band"><span>OPEN&amp;SERVE</span></div>
    <p class="brand"><span class="brand-name">Tolvanu</span><span class="brand-sub">CELLARS</span></p>
    <h2 class="flavour">florquena</h2>
    <p class="notes">Brovanza Visuales: paladar blando marrón, gráficos de clavo de olor, canela, anís estrellado, otras especias chai</p>
    <div class="medallion" role="img" aria-label="Pink lychee flower illustration"></div>
    <p class="specs"><span>12% alc/vol</span><span>750 ml</span></p>
  </section>

</main>
</body>
</html>
```